Real Estate Business Cards

Looking for a clean, sharp and professional look for our Real Estate investment Fund that invests in Multi Family Apartment buildings.

Target Market(s)

Real Estate Fund

Industry/Entity Type

Real Estate

Contact Information for Business Card

Company Description: Real Estate Investment Fund
Company Name: RKW Holdings
Name: Marcus Olvane
Cell: (917) 482-0657
Email: marcus@rkwholdings-example.com
Website: www.rkwholdings-example.com
Address: 418, 9th Street, Brooklyn NY 11218

Colors

Designer to choose colors to be used in the design.

Requirements
Nice to have
• Colors to match logo

```html
<!DOCTYPE html>
<html lang="en">
<head>
<meta charset="utf-8">
<title>RKW Holdings – Business Cards</title>
<link rel="stylesheet" href="https://fonts.googleapis.com/css2?family=EB+Garamond:wght@500&family=Montserrat:wght@400;600&family=Roboto:wght@300&family=Roboto+Condensed:wght@500&display=swap">
<style>
  :root {
    --backdrop: #eceded;
    --brand-blue: #0f73aa;
    --charcoal: #4a4a4a;
    --paper: #ffffff;
    --text-grey: #555555;
    --icon-grey: #444444;
  }
  * { margin: 0; padding: 0; box-sizing: border-box; }
  html, body {
    width: 1200px; height: 1200px; overflow: hidden;
    background: var(--backdrop);
  }
  .canvas { position: relative; width: 1200px; height: 1200px; }

  .card {
    position: absolute; left: 184px; width: 833px; height: 469px;
    overflow: hidden;
  }
  .card-band {
    position: absolute; left: 0; right: 0; bottom: 0; height: 51px;
    background: var(--charcoal);
  }

  /* Front */
  .card-front { top: 107px; background: var(--brand-blue); }
  .front-mark {
    position: absolute; left: 50%; top: 172px; width: 54px; height: 54px;
    margin-left: -27px; background: var(--paper);
  }
  .front-name {
    position: absolute; left: 0; right: 0; top: 268px; text-align: center;
    font-family: "EB Garamond", serif; font-weight: 500; font-size: 50px;
    letter-spacing: 2px; color: var(--paper); text-transform: uppercase;
  }
  .front-tagline {
    position: absolute; left: 0; right: 0; top: 0; height: 100%;
    display: flex; align-items: center; justify-content: center;
    font-family: "Roboto Condensed", sans-serif; font-weight: 500;
    font-size: 20px; letter-spacing: 1.6px; color: var(--paper);
  }

  /* Back */
  .card-back { top: 623px; background: var(--paper); }
  .back-brand {
    position: absolute; left: 0; right: 0; top: 64px;
    display: flex; align-items: center; justify-content: center; gap: 22px;
  }
  .back-mark { width: 44px; height: 44px; background: var(--brand-blue); }
  .back-name {
    font-family: "EB Garamond", serif; font-weight: 500; font-size: 46px;
    letter-spacing: 2px; color: var(--charcoal); text-transform: uppercase;
  }

  .holder {
    position: absolute; left: 230px; top: 201px; width: 170px; text-align: right;
  }
  .holder-icon { position: absolute; left: 0; top: 4px; width: 22px; height: 22px; }
  .holder-name {
    font-family: "Montserrat", sans-serif; font-weight: 600; font-size: 22px;
    letter-spacing: 0.8px; color: var(--charcoal); line-height: 30px;
  }
  .holder-company {
    font-family: "Roboto", sans-serif; font-weight: 300; font-size: 17px;
    color: var(--text-grey); line-height: 22px;
  }
  .holder-rule {
    display: block; margin: 6px 0 0 auto; width: 60px; height: 4px;
    background: var(--charcoal);
  }

  .contacts { position: absolute; left: 466px; top: 210px; list-style: none; }
  .contact {
    position: relative; padding-left: 46px;
    font-family: "Montserrat", sans-serif; font-weight: 400; font-size: 16px;
    letter-spacing: 0.9px; color: var(--text-grey); line-height: 21px;
  }
  .contact + .contact { margin-top: 11px; }
  .contact-icon { position: absolute; left: 0; top: 0; width: 22px; height: 22px; fill: var(--icon-grey); }
  .contact-address { margin-bottom: 2px; }
  .contact-phone { margin-top: 9px !important; }
  .contact-email, .contact-web { margin-top: 20px !important; }
</style>
</head>
<body>
<main class="canvas">

  <section class="card card-front" aria-label="Business card front">
    <div class="front-mark"></div>
    <div class="front-name">RKW Holdings</div>
    <div class="card-band">
      <div class="front-tagline">Real Estate Investment Fund</div>
    </div>
  </section>

  <section class="card card-back" aria-label="Business card back">
    <div class="back-brand">
      <div class="back-mark"></div>
      <div class="back-name">RKW Holdings</div>
    </div>

    <div class="holder">
      <svg class="holder-icon" viewBox="0 0 24 24" fill="#444"><circle cx="12" cy="7" r="5"/><path d="M2 23c0-6 4-9 10-9s10 3 10 9z"/></svg>
      <div class="holder-name">Marcus Olvane</div>
      <div class="holder-company">RKW Holdings</div>
      <span class="holder-rule"></span>
    </div>

    <ul class="contacts">
      <li class="contact contact-address">
        <svg class="contact-icon" viewBox="0 0 24 24"><path d="M12 2 1 11h3v11h16V11h3zM12 5.5 18.5 11v9h-13v-9z"/><path d="M12 10a3.2 3.2 0 0 0-3.2 3.2c0 2.4 3.2 5.8 3.2 5.8s3.2-3.4 3.2-5.8A3.2 3.2 0 0 0 12 10zm0 4.5a1.3 1.3 0 1 1 0-2.6 1.3 1.3 0 0 1 0 2.6z"/></svg>
        418, 9th Street,<br>Brooklyn NY 11218
      </li>
      <li class="contact contact-phone">
        <svg class="contact-icon" viewBox="0 0 24 24"><path d="M6.6 10.8a15 15 0 0 0 6.6 6.6l2.2-2.2a1 1 0 0 1 1-.25 11.4 11.4 0 0 0 3.6.6 1 1 0 0 1 1 1V20a1 1 0 0 1-1 1A17 17 0 0 1 3 4a1 1 0 0 1 1-1h3.5a1 1 0 0 1 1 1c0 1.25.2 2.45.6 3.6a1 1 0 0 1-.25 1z"/></svg>
        (917) 482-0657
      </li>
      <li class="contact contact-email">
        <svg class="contact-icon" viewBox="0 0 24 24"><path d="M2 5h20v14H2zm2 2v.5l8 5.5 8-5.5V7zm0 3v7h16v-7l-8 5.5z"/></svg>
        marcus@rkwholdings-example.com
      </li>
      <li class="contact contact-web">
        <svg class="contact-icon" viewBox="0 0 24 24"><path d="M12 2a10 10 0 1 0 0 20 10 10 0 0 0 0-20zm6.9 6h-3a15 15 0 0 0-1.3-3.7A8 8 0 0 1 18.9 8zM12 4c.8 1.1 1.5 2.5 1.9 4h-3.8c.4-1.5 1.1-2.9 1.9-4zM4.3 14a8 8 0 0 1 0-4h3.3a16 16 0 0 0 0 4zm.8 2h3a15 15 0 0 0 1.3 3.7A8 8 0 0 1 5.1 16zm3-8h-3a8 8 0 0 1 4.3-3.7A15 15 0 0 0 8.1 8zM12 20c-.8-1.1-1.5-2.5-1.9-4h3.8c-.4 1.5-1.1 2.9-1.9 4zm2.3-6H9.7a14 14 0 0 1 0-4h4.6a14 14 0 0 1 0 4zm.3 5.7a15 15 0 0 0 1.3-3.7h3a8 8 0 0 1-4.3 3.7zm1.8-5.7a16 16 0 0 0 0-4h3.3a8 8 0 0 1 0 4z"/></svg>
        www.rkwholdings-example.com
      </li>
    </ul>

    <div class="card-band"></div>
  </section>

</main>
</body>
</html>
```